The Harvest Ledger App - Modernization & Graphics User Interface Friendliness Updates

We are Harvest Ledger, and we want to bring a new branding look and graphical user interface to the Harvest Ledger App. The app is a quick reference encyclopedia for all things produce. Boasting articles on over 2,000 produce items, with information ranging from taste and application to geographical and cultural significance. Included in its features are over 10 thousand recipes, and the Harvest Ledger App Crop Bazaar – a global initiative to connect farmer, customer, and chef in one sustainable and easy to use application. The design needs to bring a greater sense of social connection – encouraging the user to participate in the 'Crop Bazaar' experience voluntarily. The design should reflect a sense of authority reflecting the authenticity and reliability of the provided information, it's writing, and its sources. Download the App here: hvldg.example/get

Target Market(s)

Women and Men between ages 21-55.

Industry/Entity Type

Education

Font styles to use
Serif
Sans Serif

Colors

Designer to choose colors to be used in the design.

Requirements
Must have
• An updated user interface, the intuitive usability of the app is currently non-existent. We are looking to reflect as the authority on produce. The app design must reflect a professional, user-friendly, up-to-date, and trustworthy feel.
Nice to have
• To incorporate the social draw of the Crop Bazaar we would like to include on the home page "Social Bubbles" (think Pictaloo stories) which updates with shared photos of produce and their location.
Should not have
• An overly complicated theme, distracting or unprofessional colors, and images.

```html
<!DOCTYPE html>
<html lang="en">
<head>
<meta charset="utf-8">
<title>Harvest Ledger App – Splash Screen</title>
<link rel="stylesheet" href="https://fonts.googleapis.com/css2?family=Cinzel:wght@600&family=Dancing+Script:wght@500&display=swap">
<style>
  :root {
    --page-bg: #2a2a2c;
    --wood-light: #8a7f74;
    --wood-mid: #5e554d;
    --wood-dark: #332d29;
    --ink: #1c1a19;
    --cream: #f6f1e8;
    --produce-red: #8c1f16;
    --produce-gold: #b9902f;
    --produce-deep: #1e1512;
    --accent-green: #3f8a3a;
  }
  html, body {
    margin: 0;
    padding: 0;
    width: 1200px;
    height: 1174px;
    overflow: hidden;
    background: var(--page-bg);
  }
  .splash-screen {
    position: absolute;
    left: 290px;
    top: 37px;
    width: 620px;
    height: 1100px;
    border-radius: 28px;
    overflow: hidden;
    box-shadow: 0 24px 60px rgba(0,0,0,0.45);
  }
  .wood-backdrop {
    position: absolute;
    inset: 0;
    background:
      linear-gradient(160deg, var(--wood-light) 0%, var(--wood-mid) 45%, var(--wood-dark) 100%);
  }
  .produce-spread {
    position: absolute;
    inset: 0;
    clip-path: polygon(0 52%, 38% 56%, 62% 72%, 100% 86%, 100% 100%, 0 100%);
    background:
      radial-gradient(ellipse at 30% 78%, var(--produce-gold) 0%, transparent 38%),
      radial-gradient(ellipse at 18% 62%, var(--produce-red) 0%, transparent 32%),
      radial-gradient(ellipse at 70% 92%, var(--produce-red) 0%, transparent 30%),
      linear-gradient(180deg, #4a2a1d 0%, var(--produce-deep) 100%);
  }
  .brand-block {
    position: absolute;
    top: 150px;
    left: 0;
    right: 0;
    text-align: center;
  }
  .brand-name {
    display: inline-flex;
    align-items: center;
    gap: 16px;
    font-family: "Cinzel", serif;
    font-weight: 600;
    font-size: 50px;
    letter-spacing: 2px;
    color: var(--ink);
    margin: 0;
  }
  .brand-mark {
    width: 22px;
    height: 22px;
    border-radius: 50%;
    background: var(--accent-green);
  }
  .brand-url {
    margin: 14px 0 0;
    font-family: "Cinzel", serif;
    font-weight: 600;
    font-size: 17px;
    letter-spacing: 4px;
    color: var(--ink);
  }
  .tagline {
    position: absolute;
    top: 340px;
    left: 0;
    right: 0;
    margin: 0;
    text-align: center;
    font-family: "Dancing Script", cursive;
    font-weight: 500;
    font-size: 50px;
    line-height: 1.25;
    color: var(--cream);
    text-shadow: 0 2px 6px rgba(0,0,0,0.35);
  }
</style>
</head>
<body>
  <main class="splash-screen">
    <div class="wood-backdrop" role="img" aria-label="Weathered grey-brown wooden table surface"></div>
    <div class="produce-spread" role="img" aria-label="Overhead photo of fresh produce on the table: red peppers, corn cobs, apples, an orange, grapes, chillies and a wooden spoon"></div>

    <header class="brand-block">
      <h1 class="brand-name"><span class="brand-mark"></span>Harvest Ledger</h1>
      <p class="brand-url">www.harvestledger.example</p>
    </header>

    <p class="tagline">Sharing the story of<br>fruits and vegetables</p>
  </main>
</body>
</html>
```